VELDA NUTRITION WEBSITE DESIGN

We need a full design for the website to present the company to customers and partners.
We are ' Velda nutrition" based in New York. We develop Multivitamins, minerals and nutritional supplements to support immunity, general health and longevity. Our products include: Pregnancy supplements, Bone supplements and Iron supplements.
The design should convey trust, natural, health and growth, also relating to the different products that we sell.

I can not download the edited design and the designer didnt submit the last revised version yet.

```html
<!DOCTYPE html>
<html lang="en">
<head>
<meta charset="utf-8">
<title>Velda Nutrition</title>
<link href="https://fonts.googleapis.com/css2?family=Bree+Serif&family=Nunito:wght@400;600;700;800&display=swap" rel="stylesheet">
<style>
:root{
  --green:#7dc143;
  --green-dark:#5e9f2a;
  --ink:#1d1d1d;
  --text:#444;
  --muted:#777;
  --blue:#1f3f8c;
  --bg-light:#f3f5f3;
  --white:#fff;
  --black:#050505;
  --star:#f5a623;
}
*{box-sizing:border-box;margin:0;padding:0}
html,body{width:1200px;height:4067px;overflow:hidden;background:var(--white)}
body{font-family:"Nunito",sans-serif;color:var(--text)}
.page{position:relative;width:1200px;height:4067px;overflow:hidden}
.abs{position:absolute}
.heading{font-family:"Bree Serif",serif;font-weight:400;line-height:1.05}
.heading .accent{color:var(--green)}
.btn{position:absolute;background:var(--green);color:var(--ink);font-weight:800;font-size:21px;display:flex;align-items:center;justify-content:center;border-radius:24px 0 24px 0;box-shadow:4px 5px 0 rgba(0,0,0,.08)}
.brand{font-family:"Nunito",sans-serif;font-weight:800;color:var(--green);display:flex;align-items:center;gap:12px;white-space:nowrap}
.brand .dot{width:34px;height:34px;border-radius:50%;background:var(--green);flex:0 0 auto}
.section-mark{position:absolute;width:62px;height:62px;border-radius:50%;background:var(--green)}
/* header */
.topbar{left:380px;top:0;width:820px;height:55px;background:var(--green);border-bottom-left-radius:40px;display:flex;align-items:center;gap:18px;padding-left:50px;color:var(--ink);font-weight:700;font-size:15px}
.topbar .item{display:flex;align-items:center;gap:10px}
.ico-dark{width:24px;height:24px;border-radius:50%;background:var(--ink);display:flex;align-items:center;justify-content:center}
.topbar .social{display:flex;gap:22px;margin-left:30px}
.topbar .sep{color:rgba(0,0,0,.4)}
.nav{left:378px;top:70px;display:flex;align-items:center;font-size:16px;font-weight:700;color:var(--ink)}
.nav a{color:inherit;text-decoration:none;margin-right:65px}
.nav a.active{color:var(--green);text-decoration:underline}
.nav .contact{background:var(--green);padding:12px 22px;border-radius:18px 0 18px 0;margin-right:0;margin-left:-5px}
/* photo placeholders */
.photo{border-radius:0;overflow:hidden}
.hero{left:0;top:124px;width:1200px;height:720px;background:linear-gradient(90deg,#e6e1d9 0%,#eeece7 50%,#f1f2ef 100%)}
.hero-photo{left:0;top:124px;width:470px;height:640px;background:linear-gradient(160deg,#efe6dc 0%,#e3cdb8 45%,#d9bfa6 70%,#ebe7e1 100%)}
.hero-title{left:497px;top:192px;font-size:47px;color:var(--ink);white-space:nowrap}
.hero-text{left:497px;top:253px;width:580px;font-size:15px;line-height:1.75;color:var(--text)}
.bottles{left:612px;top:378px;width:555px;height:382px;border-radius:28px;background:linear-gradient(180deg,#fafafa 0%,#ededed 100%);box-shadow:0 14px 28px rgba(0,0,0,.10)}
.bottles .tint{position:absolute;left:175px;top:0;width:200px;height:100%;border-radius:28px;background:linear-gradient(180deg,#f7f7f7 0%,#f2dede 100%)}
/* about */
.about-title{left:200px;top:900px;font-size:40px;color:var(--ink)}
.about-text{left:112px;top:995px;width:495px;font-size:15.5px;line-height:31px;text-align:justify;color:var(--text)}
.about-text p+p{margin-top:31px}
.about-photo{left:672px;top:912px;width:425px;height:425px;border-radius:50%;border:8px solid var(--green);background:linear-gradient(135deg,#e9d3bd 0%,#d8b796 45%,#bcd3df 100%)}
/* products */
.products{left:0;top:1415px;width:1200px;height:790px;background:linear-gradient(180deg,#8ccb4f 0%,#7fc043 60%,#78bb3c 100%)}
.products-title{left:0;top:1497px;width:1200px;text-align:center;font-size:40px;color:var(--white)}
.products-sub{left:210px;top:1595px;width:780px;text-align:center;font-size:15.5px;line-height:30px;font-weight:700;color:#f4ffe9}
.card{top:1673px;width:287px;height:352px;background:var(--white);border-radius:8px;box-shadow:0 6px 18px rgba(0,0,0,.12)}
.card .img{position:absolute;left:78px;top:30px;width:132px;height:240px;border-radius:18px}
.card .name{position:absolute;left:0;top:294px;width:100%;text-align:center;font-weight:800;font-size:15.5px;color:var(--ink)}
.card .stars{position:absolute;left:0;top:318px;width:100%;text-align:center;color:var(--star);font-size:16px;letter-spacing:1px}
.card .tools{position:absolute;right:16px;top:30px;display:flex;flex-direction:column;gap:24px}
.card .tools span{width:28px;height:28px;border-radius:50%;border:1px solid #ddd;display:flex;align-items:center;justify-content:center}
/* features */
.feature-bottle{left:478px;top:2250px;width:244px;height:465px;border-radius:40px 40px 30px 30px;background:linear-gradient(180deg,#f8f8f8 0%,#eceef3 55%,#e3e7f0 100%);box-shadow:0 12px 26px rgba(0,0,0,.10)}
.feature-caption{left:0;top:2740px;width:1200px;text-align:center;font-weight:800;font-size:21px;color:var(--ink)}
.feat{position:absolute;width:360px;display:flex;align-items:center;gap:18px;font-size:19px;line-height:31px;color:var(--ink)}
.feat strong{color:var(--blue);font-weight:800}
.feat.left{left:80px;justify-content:flex-end;text-align:right}
.feat.right{left:762px}
.feat .ic{flex:0 0 auto;width:78px;height:78px;border-radius:50%;background:var(--white);box-shadow:0 2px 10px rgba(0,0,0,.12);display:flex;align-items:center;justify-content:center}
/* testimonials */
.testi-title{left:516px;top:2938px;font-size:40px;color:var(--ink)}
.avatar{border-radius:50%;background:linear-gradient(160deg,#eadccd 0%,#d6b99d 100%);border:4px solid #fff;box-shadow:0 4px 12px rgba(0,0,0,.12)}
.t-name{left:0;top:3208px;width:1200px;text-align:center;font-family:"Bree Serif",serif;font-size:25px;color:var(--green)}
.t-loc{left:0;top:3245px;width:1200px;text-align:center;font-size:12px;color:var(--muted);font-weight:700}
.t-stars{left:0;top:3262px;width:1200px;text-align:center;color:var(--star);font-size:30px;letter-spacing:2px}
.t-text{left:250px;top:3302px;width:700px;text-align:center;font-size:15px;line-height:27px;color:var(--text)}
.quote{font-family:"Bree Serif",serif;font-size:220px;color:#cfcfcf;line-height:1}
/* footer */
.follow{left:112px;top:3668px;display:flex;align-items:center;gap:18px;color:var(--white);font-weight:800;font-size:21px}
.follow .s{width:30px;height:30px;border-radius:50%;background:var(--green)}
.subscribe{left:548px;top:3662px;width:540px;height:56px;background:var(--white);border-radius:28px;overflow:hidden}
.subscribe span{position:absolute;left:40px;top:19px;font-size:13px;color:#555}
.subscribe b{position:absolute;right:0;top:0;width:178px;height:56px;background:var(--green);color:var(--ink);font-size:22px;font-weight:700;display:flex;align-items:center;justify-content:center}
.rule{left:112px;top:3760px;width:976px;height:1px;background:#5a5a5a}
.f-col{top:3800px;color:var(--white)}
.f-col h4{font-weight:600;font-size:21px;margin-bottom:18px}
.f-col li{list-style:none;display:flex;align-items:center;gap:12px;font-size:16px;margin-bottom:12px;color:#eee}
.f-col .arr{width:16px;height:16px;border-radius:50%;background:var(--white);display:flex;align-items:center;justify-content:center}
.f-contact li{align-items:flex-start;margin-bottom:22px;line-height:27px}
.f-contact .ci{flex:0 0 auto;width:34px;height:34px;border-radius:50%;background:var(--green);display:flex;align-items:center;justify-content:center}
.copy{left:110px;top:3917px;font-size:11px;font-weight:700;color:var(--white)}
</style>
</head>
<body>
<div class="page">

  <!-- header -->
  <div class="abs brand" style="left:95px;top:38px;font-size:30px;"><span class="dot"></span>Velda Nutrition</div>
  <div class="abs topbar">
    <div class="item"><span class="ico-dark"><svg width="12" height="12" viewBox="0 0 24 24"><path fill="#fff" d="M6.6 10.8a15 15 0 006.6 6.6l2.2-2.2a1 1 0 011-.25 11 11 0 003.6.6 1 1 0 011 1V20a1 1 0 01-1 1A17 17 0 013 4a1 1 0 011-1h3.5a1 1 0 011 1c0 1.25.2 2.45.6 3.6a1 1 0 01-.25 1z"/></svg></span>+1 555 014 2290</div>
    <span class="sep">|</span>
    <div class="item"><span class="ico-dark"><svg width="12" height="12" viewBox="0 0 24 24"><path fill="#fff" d="M3 5h18v14H3z"/><path d="M3 5l9 7 9-7" stroke="#1d1d1d" stroke-width="2" fill="none"/></svg></span>hello@veldanutrition.com</div>
    <span class="sep">|</span>
    <div class="social"><span class="ico-dark"></span><span class="ico-dark"></span><span class="ico-dark"></span><span class="ico-dark"></span></div>
  </div>
  <nav class="abs nav">
    <a class="active" href="#">Home</a><a href="#">About</a><a href="#">Services</a><a href="#">Testimonials</a><a href="#">Blog</a><a class="contact" href="#">Contact Us</a>
  </nav>

  <!-- hero -->
  <div class="abs hero"></div>
  <div class="abs hero-photo" role="img" aria-label="Smiling young woman holding a supplement capsule"></div>
  <h1 class="abs heading hero-title">Welcome To <span class="accent">Velda Nutrition</span></h1>
  <p class="abs hero-text">Itaque earum rerum hic tenetur a sapiente delectus, ut aut reiciendis voluptatibus maiores alias consequatur aut perferendis doloribus asperiores repellat.</p>
  <div class="btn" style="left:500px;top:318px;width:165px;height:52px;">Get Started</div>
  <div class="abs bottles" role="img" aria-label="Three supplement bottles, iron supplement in the centre"><div class="tint"></div></div>
  <svg class="abs" style="left:0;top:640px" width="1200" height="230" viewBox="0 0 1200 230" aria-hidden="true">
    <path d="M0 150 C200 70 420 60 640 110 C860 160 1050 120 1200 20 L1200 230 L0 230Z" fill="var(--green)"/>
    <path d="M0 175 C220 110 430 95 650 150 C860 200 1060 190 1200 95 L1200 230 L0 230Z" fill="#fff"/>
  </svg>

  <!-- about -->
  <div class="section-mark" style="left:118px;top:905px"></div>
  <h2 class="abs heading about-title">About<br><span class="accent">Velda Nutrition</span></h2>
  <div class="abs about-text">
    <p>Et harum quidem rerum facilis est et expedita distinctio. Nam libero tempore, cum soluta nobis est eligendi optio cumque nihil impedit quo minus id quod maxime placeat facere possimus, omnis voluptas assumenda est, omnis dolor repellendus.</p>
    <p>Itaque earum rerum ut aut reiciendis voluptatibus hic tenetur a sapiente delectus, ut aut reiciendis voluptatibus maiores alias consequatur aut perferendis doloribus asperiores repellat.</p>
  </div>
  <div class="btn" style="left:112px;top:1262px;width:165px;height:60px;">Read More</div>
  <div class="abs about-photo" role="img" aria-label="Three cheerful young friends posing together"></div>

  <!-- products -->
  <div class="abs products" role="img" aria-label="Green backdrop with a faded photo of friends"></div>
  <svg class="abs" style="left:0;top:1415px" width="1200" height="40" viewBox="0 0 1200 40" aria-hidden="true"><rect width="1200" height="2" fill="#fff" opacity="0"/></svg>
  <div class="section-mark" style="left:486px;top:1500px;background:#fff"></div>
  <h2 class="abs heading" style="left:576px;top:1497px;font-size:40px;color:#fff">Our<br>Product</h2>
  <p class="abs products-sub">Itaque earum rerum hic tenetur a sapiente delectus, ut aut reiciendis voluptatibus maiores alias consequatur aut perferendis doloribus asperiores repellat.</p>
  <div class="abs card" style="left:112px"><div class="img" role="img" aria-label="Bone supplement bottle with blue label" style="background:linear-gradient(180deg,#f6f6f6 0%,#e6ebf5 100%)"></div><div class="name">Velda Nutrition OsteoCore</div><div class="stars">★★★★★</div></div>
  <div class="abs card" style="left:456px;box-shadow:0 10px 30px rgba(0,0,0,.25)"><div class="img" role="img" aria-label="Pregnancy supplement bottle with purple label" style="background:linear-gradient(180deg,#f6f6f6 0%,#eee4f0 100%)"></div>
    <div class="tools">
      <span><svg width="14" height="10" viewBox="0 0 14 10"><path d="M1 5C3 1 11 1 13 5 11 9 3 9 1 5z" fill="none" stroke="#555"/><circle cx="7" cy="5" r="2" fill="#555"/></svg></span>
      <span><svg width="14" height="12" viewBox="0 0 14 12"><path d="M7 11L1.5 5.5a3 3 0 015-4L7 2l.5-.5a3 3 0 015 4z" fill="none" stroke="#555"/></svg></span>
      <span><svg width="12" height="12" viewBox="0 0 12 12"><circle cx="5" cy="5" r="3.5" fill="none" stroke="#555"/><path d="M8 8l3 3" stroke="#555"/></svg></span>
    </div>
    <div class="name">Velda Nutrition MamaBloom</div><div class="stars">★★★★★</div></div>
  <div class="abs card" style="left:801px"><div class="img" role="img" aria-label="Iron supplement bottle with red label" style="background:linear-gradient(180deg,#f6f6f6 0%,#f4e2e2 100%)"></div><div class="name">Velda Nutrition IronLeaf</div><div class="stars">★★★★★</div></div>
  <svg class="abs" style="left:0;top:2080px" width="1200" height="130" viewBox="0 0 1200 130" aria-hidden="true">
    <path d="M0 30 C250 110 520 80 760 40 C960 5 1100 20 1200 45 L1200 130 L0 130Z" fill="var(--bg-light)"/>
  </svg>

  <!-- features -->
  <div class="abs" style="left:0;top:2200px;width:1200px;height:640px;background:var(--bg-light)"></div>
  <div class="abs feature-bottle" role="img" aria-label="Bone supplement bottle, calcium and vitamin D formula"></div>
  <div class="abs feature-caption">Velda Nutrition OsteoCore</div>

  <div class="feat left" style="top:2250px"><span>Calcium &amp; vitamin D3 for<br><strong>bone strength</strong></span><span class="ic"><svg width="36" height="36" viewBox="0 0 36 36"><path d="M18 4c5 7 10 12 10 18a10 10 0 01-20 0c0-6 5-11 10-18z" fill="none" stroke="#1f3f8c" stroke-width="2"/></svg></span></div>
  <div class="feat left" style="top:2380px"><span>Highest level of<br><strong>vitamin D</strong></span><span class="ic"><svg width="36" height="36" viewBox="0 0 36 36"><circle cx="18" cy="18" r="12" fill="none" stroke="#1f3f8c" stroke-width="2"/><circle cx="18" cy="18" r="5" fill="none" stroke="#1f3f8c" stroke-width="2"/></svg></span></div>
  <div class="feat left" style="top:2509px"><span>Collagen supporting<br><strong>minerals for flexibility</strong></span><span class="ic"><svg width="36" height="36" viewBox="0 0 36 36"><path d="M18 4c5 7 10 12 10 18a10 10 0 01-20 0c0-6 5-11 10-18z" fill="none" stroke="#1f3f8c" stroke-width="2"/><path d="M18 14v16" stroke="#1f3f8c" stroke-width="2"/></svg></span></div>
  <div class="feat left" style="top:2638px"><span>Easy to swallow Calcium<br><strong>Supplements</strong></span><span class="ic"><svg width="36" height="36" viewBox="0 0 36 36"><circle cx="18" cy="18" r="13" fill="none" stroke="#1f3f8c" stroke-width="2"/><circle cx="18" cy="18" r="7" fill="none" stroke="#1f3f8c" stroke-width="2"/></svg></span></div>

  <div class="feat right" style="top:2250px"><span class="ic"><svg width="36" height="36" viewBox="0 0 36 36"><circle cx="15" cy="20" r="10" fill="none" stroke="#1f3f8c" stroke-width="2.5"/><circle cx="21" cy="16" r="10" fill="none" stroke="#1f3f8c" stroke-width="2.5"/></svg></span><span>Two in one dual action<br><strong>OsteoCore</strong></span></div>
  <div class="feat right" style="top:2380px"><span class="ic"><svg width="36" height="36" viewBox="0 0 36 36"><circle cx="18" cy="18" r="13" fill="none" stroke="#1f3f8c" stroke-width="2"/><circle cx="13" cy="15" r="2" fill="#1f3f8c"/><circle cx="22" cy="14" r="2" fill="#1f3f8c"/><circle cx="18" cy="23" r="2" fill="#1f3f8c"/></svg></span><span>Bone strength &amp; flexibility<br><strong>Supplements</strong></span></div>
  <div class="feat right" style="top:2509px"><span class="ic"><svg width="38" height="38" viewBox="0 0 38 38"><path d="M12 8l6 3.5v7L12 22l-6-3.5v-7z M26 8l6 3.5v7L26 22l-6-3.5v-7z M19 20l6 3.5v7L19 34l-6-3.5v-7z" fill="none" stroke="#1f3f8c" stroke-width="1.8"/></svg></span><span>Ingredients,calcium<br><strong>Carbonate</strong></span></div>
  <div class="feat right" style="top:2638px"><span class="ic"><svg width="36" height="36" viewBox="0 0 36 36"><path d="M18 5v26M10 10h6M20 10h6M10 26h6M20 26h6" stroke="#1f3f8c" stroke-width="2" fill="none"/></svg></span><span>Calcium 600mg+vit.D 800<br><strong>I.U.+Minerals</strong></span></div>

  <!-- testimonials -->
  <div class="section-mark" style="left:436px;top:2940px"></div>
  <h2 class="abs heading testi-title">What<br><span class="accent">Customer Says</span></h2>
  <div class="abs avatar" style="left:527px;top:3042px;width:136px;height:136px" role="img" aria-label="Portrait of customer"></div>
  <div class="abs avatar" style="left:121px;top:3118px;width:66px;height:66px" role="img" aria-label="Portrait of customer"></div>
  <div class="abs avatar" style="left:1001px;top:3046px;width:46px;height:46px" role="img" aria-label="Portrait of customer"></div>
  <div class="abs" style="left:365px;top:3156px;width:14px;height:14px;border-radius:50%;background:#e3262b"></div>
  <div class="abs" style="left:880px;top:3116px;width:7px;height:7px;border-radius:50%;background:#4a7fd8"></div>
  <div class="abs t-name">Daniel Moreno</div>
  <div class="abs t-loc">United States</div>
  <div class="abs t-stars">★★★★★</div>
  <div class="abs quote" style="left:150px;top:3195px">“</div>
  <div class="abs quote" style="left:938px;top:3270px">”</div>
  <p class="abs t-text">Itaque earum rerum hic tenetur a sapiente delectus, ut aut reiciendis voluptatibus maiores alias. Consequatur aut perferendis doloribus asperiores repellat.Et sapiente delectus, ut autharum quidem rerum facilis est et expedita distinctio.</p>

  <!-- footer -->
  <svg class="abs" style="left:0;top:3430px" width="1200" height="637" viewBox="0 0 1200 637" aria-hidden="true">
    <path d="M0 110 C220 150 520 150 760 95 C930 55 1080 40 1200 40 L1200 637 L0 637Z" fill="var(--black)"/>
    <path d="M0 35 C120 110 300 140 520 130 C620 125 690 115 760 95 C620 130 400 140 220 110 C120 95 50 75 0 60Z" fill="var(--green)"/>
  </svg>
  <div class="abs follow">Follow Us On: <span class="s"></span><span class="s"></span><span class="s"></span><span class="s"></span></div>
  <div class="abs subscribe"><span>Enter Email</span><b>Subscribe</b></div>
  <div class="abs rule"></div>

  <div class="abs brand" style="left:112px;top:3846px;font-size:28px;"><span class="dot" style="width:30px;height:30px"></span>Velda Nutrition</div>
  <div class="abs copy">Copyrights@2022.veldanutrition.All Rights Reserved</div>

  <div class="abs f-col" style="left:437px">
    <h4>Quick Link</h4>
    <ul>
      <li><span class="arr"><svg width="8" height="8" viewBox="0 0 8 8"><path d="M2 1l3 3-3 3" stroke="#000" stroke-width="1.5" fill="none"/></svg></span>Home</li>
      <li><span class="arr"><svg width="8" height="8" viewBox="0 0 8 8"><path d="M2 1l3 3-3 3" stroke="#000" stroke-width="1.5" fill="none"/></svg></span>About</li>
      <li><span class="arr"><svg width="8" height="8" viewBox="0 0 8 8"><path d="M2 1l3 3-3 3" stroke="#000" stroke-width="1.5" fill="none"/></svg></span>Product</li>
      <li><span class="arr"><svg width="8" height="8" viewBox="0 0 8 8"><path d="M2 1l3 3-3 3" stroke="#000" stroke-width="1.5" fill="none"/></svg></span>Testimonials</li>
      <li><span class="arr"><svg width="8" height="8" viewBox="0 0 8 8"><path d="M2 1l3 3-3 3" stroke="#000" stroke-width="1.5" fill="none"/></svg></span>Contact us</li>
    </ul>
  </div>
  <div class="abs f-col" style="left:642px">
    <h4>Help Links</h4>
    <ul>
      <li><span class="arr"><svg width="8" height="8" viewBox="0 0 8 8"><path d="M2 1l3 3-3 3" stroke="#000" stroke-width="1.5" fill="none"/></svg></span>FAQ</li>
      <li><span class="arr"><svg width="8" height="8" viewBox="0 0 8 8"><path d="M2 1l3 3-3 3" stroke="#000" stroke-width="1.5" fill="none"/></svg></span>Terms of use</li>
      <li><span class="arr"><svg width="8" height="8" viewBox="0 0 8 8"><path d="M2 1l3 3-3 3" stroke="#000" stroke-width="1.5" fill="none"/></svg></span>Privacy Policy</li>
      <li><span class="arr"><svg width="8" height="8" viewBox="0 0 8 8"><path d="M2 1l3 3-3 3" stroke="#000" stroke-width="1.5" fill="none"/></svg></span>Support Links</li>
      <li><span class="arr"><svg width="8" height="8" viewBox="0 0 8 8"><path d="M2 1l3 3-3 3" stroke="#000" stroke-width="1.5" fill="none"/></svg></span>Conditions</li>
    </ul>
  </div>
  <div class="abs f-col f-contact" style="left:855px">
    <h4>Contact us</h4>
    <ul>
      <li><span class="ci"><svg width="16" height="18" viewBox="0 0 24 28"><path d="M12 2a9 9 0 00-9 9c0 7 9 15 9 15s9-8 9-15a9 9 0 00-9-9z" fill="#fff"/><circle cx="12" cy="11" r="3.5" fill="#7dc143"/></svg></span><span>Veldanutrition<br>United States</span></li>
      <li><span class="ci"><svg width="16" height="16" viewBox="0 0 24 24"><path fill="#fff" d="M6.6 10.8a15 15 0 006.6 6.6l2.2-2.2a1 1 0 011-.25 11 11 0 003.6.6 1 1 0 011 1V20a1 1 0 01-1 1A17 17 0 013 4a1 1 0 011-1h3.5a1 1 0 011 1c0 1.25.2 2.45.6 3.6a1 1 0 01-.25 1z"/></svg></span><span>+1 555 014 2290</span></li>
      <li><span class="ci"><svg width="16" height="14" viewBox="0 0 24 20"><path fill="#fff" d="M2 2h20v16H2z"/><path d="M2 2l10 8 10-8" stroke="#7dc143" stroke-width="2" fill="none"/></svg></span><span>hello@veldanutrition.com</span></li>
    </ul>
  </div>

</div>
</body>
</html>
```